Brook Medical Needs a PowerPoint Design

Brook Medical needs a PowerPoint template developed for use during presentations by our marketing department. Brook offers Medical specialty services to family physicians throughout Calgary. At Brook we pride ourselves on our commitment to our patients as well as having very short wait times and convenient locations spread throughout the communities. We offer services in Pulmonary Diagnostics as well as sleep apnea assessment and treatment. Consults from medical specialties such as Respirology, Physiatry, Internal Medicine, Occupational Medicine, Pediatric Infectious Disease, and alergy are also available.

***Please note we are not looking for you to build a presentation we just want the design of the slides for us to add content as needed****

We require an updated powerpoint template that we can use in a range of situations such as during marketing presentations or professional educational events. We would like a design that is modern and unique. We would like the mountain theme built into the design elements of the slide deck

We require a whole slide deck (Title slide; etc) for the Brook Medical Group as well as a body slide for our sleep division.

Our usual font is ArnoPro Semi Bold

Our Websites: brookairway.example brookrestclinic.example

Closest pantone color for Brook’s purple is PMS 814 2X

Target Market(s)

Physicians, medical professionals

Industry/Entity Type

Medical

Font styles to use
Other font styles liked:
• ArnoPro Semi Bold

Requirements
Must have
• Similar look and feel to sleep and medical slide
Nice to have
• Mountain design built into deck.
Should not have
• large actual images of mountains.

```html
<!DOCTYPE html>
<html lang="en">
<head>
<meta charset="utf-8">
<title>Brook Medical – Print Slide</title>
<link rel="stylesheet" href="https://fonts.googleapis.com/css2?family=Montserrat:wght@300;400;500&display=swap">
<style>
  :root {
    --purple: #8e4f9e;
    --purple-soft: #c9a6d2;
    --lavender: #ece0f0;
    --ink: #1a1a1a;
    --slate: #5a7d96;
    --green: #5fb58c;
    --orange: #f39a3a;
    --red: #e2473d;
    --grid: #d9c6de;
    --body-text: #b0456a;
    --paper: #ffffff;
  }
  html, body { margin: 0; padding: 0; overflow: hidden; background: var(--paper); }
  .slide {
    position: relative; width: 849px; height: 1200px; overflow: hidden;
    background: linear-gradient(90deg, var(--purple-soft) 0%, var(--lavender) 24%, rgba(255,255,255,0) 40%), var(--paper);
    font-family: "Montserrat", Arial, sans-serif; color: var(--ink);
  }
  .emblem-area {
    position: absolute; left: 0; top: 226px; width: 226px; height: 974px;
    background: radial-gradient(ellipse at 20% 45%, rgba(142,79,158,0.22), rgba(142,79,158,0.08) 60%, rgba(142,79,158,0) 80%);
  }
  .brand {
    position: absolute; left: 28px; top: 16px; display: flex; flex-direction: column; align-items: center; gap: 4px;
    color: var(--purple); font-size: 18px; font-weight: 500;
  }
  .brand-ring { width: 86px; height: 86px; border: 2px solid var(--purple); border-radius: 50%; }
  .agenda {
    position: absolute; left: 226px; top: 60px; margin: 0; padding: 0; list-style: none;
    font-size: 58px; font-weight: 400; letter-spacing: 15px; line-height: 62px;
  }
  .growth-chart { position: absolute; left: 255px; top: 300px; }
  .trend-chart { position: absolute; left: 240px; top: 605px; }
  .chart-note {
    position: absolute; left: 290px; top: 776px; width: 400px; margin: 0;
    font-size: 12px; line-height: 15px; color: var(--body-text);
  }
  .world-map {
    position: absolute; left: 269px; top: 906px; width: 425px; height: 212px;
    background: linear-gradient(180deg, #9a5fab, var(--purple));
    border-radius: 40% 45% 35% 40%;
  }
  .map-pins { position: absolute; left: 255px; top: 905px; }
  .footer-title {
    position: absolute; left: 240px; width: 370px; top: 1128px; margin: 0; text-align: center;
    font-size: 44px; font-weight: 500; letter-spacing: 1px; line-height: 50px;
  }
</style>
</head>
<body>
<main class="slide">
  <div class="emblem-area" role="img" aria-label="Faint medical emblem decoration"></div>

  <div class="brand"><span class="brand-ring"></span><span>Brook</span></div>

  <ol class="agenda">
    <li>1.TEXT</li>
    <li>2.TEXT</li>
    <li>3.TEXT</li>
    <li>4.TEXT</li>
  </ol>

  <svg class="growth-chart" width="450" height="230" viewBox="255 300 450 230" aria-label="Growth chart">
    <defs>
      <clipPath id="growth-area">
        <path d="M269,518 L269,512 C450,500 600,450 694,334 L694,518 Z"/>
      </clipPath>
    </defs>
    <g clip-path="url(#growth-area)">
      <rect x="269" y="300" width="106" height="220" fill="var(--slate)"/>
      <rect x="375" y="300" width="125" height="220" fill="var(--green)"/>
      <rect x="500" y="300" width="90" height="220" fill="var(--orange)"/>
      <rect x="590" y="300" width="104" height="220" fill="var(--red)"/>
    </g>
    <g stroke-width="2">
      <line x1="300" y1="332" x2="300" y2="510" stroke="var(--slate)"/>
      <line x1="440" y1="332" x2="440" y2="496" stroke="var(--green)"/>
      <line x1="555" y1="332" x2="555" y2="462" stroke="var(--orange)"/>
      <line x1="675" y1="332" x2="675" y2="356" stroke="var(--red)"/>
    </g>
    <g font-size="13" text-anchor="middle" font-family="Montserrat, Arial, sans-serif">
      <text x="300" y="326" fill="var(--slate)">15%</text>
      <text x="440" y="326" fill="var(--green)">31%</text>
      <text x="555" y="326" fill="var(--orange)">45%</text>
      <text x="675" y="326" fill="var(--red)">77%</text>
    </g>
  </svg>

  <svg class="trend-chart" width="470" height="170" viewBox="240 605 470 170" aria-label="Trend chart">
    <g stroke="var(--grid)" stroke-dasharray="3 3" stroke-width="1">
      <line x1="272" y1="620" x2="694" y2="620"/>
      <line x1="272" y1="650" x2="694" y2="650"/>
      <line x1="272" y1="680" x2="694" y2="680"/>
      <line x1="272" y1="710" x2="694" y2="710"/>
      <line x1="272" y1="740" x2="694" y2="740"/>
      <line x1="272" y1="620" x2="272" y2="760"/>
    </g>
    <line x1="272" y1="760" x2="694" y2="760" stroke="var(--purple)" stroke-width="1.5"/>
    <g font-size="11" fill="var(--purple)" font-family="Montserrat, Arial, sans-serif">
      <text x="242" y="624">100%</text>
      <text x="252" y="764">0%</text>
    </g>
    <g fill="var(--paper)" stroke-width="2">
      <polyline points="285,745 325,700 365,660 405,690 445,645 485,695 525,680 565,668 605,700 645,650 690,622" fill="none" stroke="var(--orange)"/>
      <polyline points="285,762 325,748 365,735 405,758 445,730 485,722 525,742 565,740 605,745 645,732 690,700" fill="none" stroke="var(--red)"/>
      <g stroke="var(--orange)">
        <circle cx="325" cy="700" r="4"/><circle cx="365" cy="660" r="4"/><circle cx="405" cy="690" r="4"/>
        <circle cx="445" cy="645" r="4"/><circle cx="485" cy="695" r="4"/><circle cx="525" cy="680" r="4"/>
        <circle cx="565" cy="668" r="4"/><circle cx="605" cy="700" r="4"/><circle cx="645" cy="650" r="4"/><circle cx="690" cy="622" r="4"/>
      </g>
      <g stroke="var(--red)">
        <circle cx="325" cy="748" r="4"/><circle cx="365" cy="735" r="4"/><circle cx="405" cy="758" r="4"/>
        <circle cx="445" cy="730" r="4"/><circle cx="485" cy="722" r="4"/><circle cx="525" cy="742" r="4"/>
        <circle cx="565" cy="740" r="4"/><circle cx="605" cy="745" r="4"/><circle cx="645" cy="732" r="4"/><circle cx="690" cy="700" r="4"/>
      </g>
    </g>
  </svg>

  <p class="chart-note">Lorem ipsum dolor sit amet, consectetur adipiscing elit, sed do eiusmod tempor incididunt ut labore et dolore magna aliqua.</p>

  <div class="world-map" role="img" aria-label="World map in purple"></div>

  <svg class="map-pins" width="455" height="225" viewBox="0 0 455 225" aria-label="Regional percentages">
    <g font-size="12" text-anchor="middle" font-family="Montserrat, Arial, sans-serif" stroke-width="2.5">
      <g stroke="var(--slate)" fill="var(--paper)"><circle cx="42" cy="45" r="15"/><line x1="42" y1="60" x2="42" y2="78"/></g>
      <text x="42" y="49" fill="var(--slate)">24%</text>
      <g stroke="var(--red)" fill="var(--paper)"><circle cx="165" cy="30" r="15"/><line x1="165" y1="45" x2="165" y2="63"/></g>
      <text x="165" y="34" fill="var(--red)">71%</text>
      <g stroke="var(--orange)" fill="var(--paper)"><circle cx="115" cy="150" r="15"/><line x1="115" y1="135" x2="115" y2="118"/></g>
      <text x="115" y="154" fill="var(--orange)">33%</text>
      <g stroke="var(--green)" fill="var(--paper)"><circle cx="408" cy="125" r="15"/><line x1="408" y1="140" x2="408" y2="158"/></g>
      <text x="408" y="129" fill="var(--green)">17%</text>
    </g>
  </svg>

  <h1 class="footer-title">PRINT SLIDE</h1>
</main>
</body>
</html>
```